Retirement Plan Advisor Bio

See the attached document and photo for content. I would like someone to design this one page flyer using my logo. This logo was designed by a designer with sketch hive. I am looking for a professional looking document. I want to he color scheme to be primarily white and gold.

Target Market(s)

Employers who offer a retirement plan

Requirements
Should not have
• The designs that I have received look more like resumes. I am interested in advertising my Retirement plan services. If anyone can change their submissions and change it to an ad for retirement plan services instead of a Bio or resume, I would prefer that.

```html
<!DOCTYPE html>
<html lang="en">
<head>
<meta charset="utf-8">
<title>Retirement Saving Plan – Vero Financial</title>
<link href="https://fonts.googleapis.com/css2?family=Montserrat:wght@700;800&family=Open+Sans:wght@400;600;700&display=swap" rel="stylesheet">
<style>
  :root {
    --gold: #a8884c;
    --gold-light: #bfa46c;
    --gold-pale: #cdb788;
    --grey: #808285;
    --ink: #231f20;
    --white: #ffffff;
  }
  * { margin: 0; padding: 0; box-sizing: border-box; }
  html, body { width: 927px; height: 1200px; overflow: hidden; background: var(--white); }
  .flyer {
    position: relative; width: 927px; height: 1200px; overflow: hidden;
    background: var(--white); font-family: "Open Sans", Arial, sans-serif; color: var(--ink);
  }
  .abs { position: absolute; }

  .brand {
    left: 116px; top: 78px; display: flex; align-items: center; gap: 12px;
    color: var(--gold); font-family: "Open Sans", Arial, sans-serif; font-weight: 600;
    font-size: 34px; letter-spacing: 0.5px;
  }
  .brand-square { width: 26px; height: 26px; background: var(--gold); }

  .hero-photo {
    left: 0; top: 163px; width: 927px; height: 426px;
    background: linear-gradient(180deg, #e9d9c0 0%, #d9c4a3 28%, #9fa3a0 42%, #c99a5c 62%, #e0a862 100%);
  }

  .shapes { left: 0; top: 0; width: 927px; height: 1200px; }

  .headline {
    left: 68px; top: 482px; color: var(--white);
    font-family: "Montserrat", Arial, sans-serif; font-weight: 800;
    font-size: 53px; line-height: 54px; letter-spacing: 0.5px;
  }
  .tagline {
    left: 72px; top: 600px; color: var(--white);
    font-family: "Open Sans", Arial, sans-serif; font-weight: 700; font-size: 30px;
  }

  .portrait-frame {
    left: 619px; top: 437px; width: 202px; height: 202px; border-radius: 50%;
    background: var(--white); padding: 8px;
  }
  .portrait {
    width: 100%; height: 100%; border-radius: 50%;
    background: radial-gradient(circle at 50% 45%, #d9c6a8 0%, #b89f7d 30%, #5d7597 60%, #3f5676 100%);
  }

  .advisor { left: 583px; top: 644px; }
  .advisor-name {
    color: var(--gold); font-weight: 700; font-size: 29px; line-height: 36px;
  }
  .advisor-name small { color: var(--ink); font-weight: 400; font-size: 11px; margin-left: 8px; vertical-align: 10px; }
  .advisor-role { font-size: 19px; line-height: 26px; }

  .intro {
    left: 68px; top: 690px; width: 450px; color: var(--grey);
    font-weight: 700; font-size: 23px; line-height: 27.4px; white-space: nowrap;
  }

  .section-title { color: var(--gold); font-weight: 700; font-size: 18px; margin-bottom: 6px; }
  .list { list-style: none; font-size: 13.4px; line-height: 18px; }
  .list li { position: relative; padding-left: 17px; margin-bottom: 4.5px; }
  .dot-list li::before {
    content: ""; position: absolute; left: 0; top: 5px; width: 7px; height: 7px;
    border-radius: 50%; background: var(--gold-light);
  }
  .tick-list li svg { position: absolute; left: 0; top: 4px; width: 12px; height: 10px; }

  .qualifications { left: 583px; top: 725px; width: 300px; }
  .education { left: 583px; top: 918px; width: 320px; }
  .specialties { left: 68px; top: 910px; width: 450px; }

  .cta {
    left: 55px; top: 1109px; color: var(--grey);
    font-weight: 700; font-size: 21.5px; letter-spacing: 0.2px;
  }
  .address-bar {
    left: 53px; top: 1151px; color: var(--white); font-weight: 600; font-size: 14.5px;
    display: flex; gap: 30px;
  }

  .contact { left: 554px; top: 1100px; display: flex; gap: 14px; color: var(--white); }
  .contact-icon { width: 54px; height: 56px; margin-top: 4px; }
  .contact-phone { font-family: "Open Sans", Arial, sans-serif; font-weight: 700; font-size: 38px; line-height: 42px; }
  .contact-email { font-weight: 700; font-size: 21px; line-height: 26px; white-space: nowrap; }
</style>
</head>
<body>
<main class="flyer">
  <div class="abs hero-photo" role="img" aria-label="Photo of a retired couple relaxing in colourful beach chairs on a sandy shore at sunset"></div>

  <svg class="abs shapes" viewBox="0 0 927 1200" aria-hidden="true">
    <polygon points="678,0 927,0 927,162 631,162" fill="var(--gold)"/>
    <polygon points="0,447 577,447 530,662 0,662" fill="var(--gold-pale)"/>
    <polygon points="0,447 573,447 516,662 0,662" fill="var(--gold)"/>
    <polygon points="516,662 927,662 927,589 536,589" fill="var(--white)"/>
    <polygon points="0,1145 522,1145 514,1180 0,1180" fill="var(--gold)"/>
    <polygon points="541,1084 927,1084 927,1200 512,1200" fill="var(--gold-light)"/>
  </svg>

  <div class="abs brand"><span class="brand-square"></span>Vero Financial, LLC</div>

  <h1 class="abs headline">RETIREMENT<br>SAVING PLAN</h1>
  <p class="abs tagline">Start saving , Enjoy life</p>

  <div class="abs portrait-frame">
    <div class="portrait" role="img" aria-label="Portrait photo of the financial advisor"></div>
  </div>

  <div class="abs advisor">
    <div class="advisor-name">Claire M Holden<small>CFP®AIF®</small></div>
    <div class="advisor-role">Keystone Financial Advisor</div>
  </div>

  <p class="abs intro">I strive to improve retirement<br>outcomes for my plan sponsor clients<br>and their employees through careful<br>retirement plan design assistance,<br>strategic and targeted communication<br>and education , as well as continual<br>monitoring of results.</p>

  <section class="abs qualifications">
    <h2 class="section-title">Qualifications</h2>
    <ul class="list dot-list">
      <li>Certified Financial Planner®</li>
      <li>Accredited Investment Fiduciary®</li>
      <li>Investment Advisor Representative</li>
      <li>Series 7, 63, and 65 Securities licenses with Keystone Financial</li>
      <li>Holds Life and Health Insurance licenses from Illinois</li>
    </ul>
  </section>

  <section class="abs education">
    <h2 class="section-title">Education</h2>
    <ul class="list dot-list">
      <li>BS Bradwell University, 1987</li>
      <li>*Securities and Investment Advisory Services offered through Keystone Financial Holdings, Inc, a Registered Broker/Dealer and Investment Advisor, member NSRA/ISPC</li>
    </ul>
  </section>

  <section class="abs specialties">
    <h2 class="section-title">Professional Specialties</h2>
    <ul class="list tick-list">
      <li><svg viewBox="0 0 12 10"><path d="M1 5.5 4.5 9 11 1.5" fill="none" stroke="var(--gold)" stroke-width="2.4"/></svg>Over 18 years of experience in the retirement plan industry</li>
      <li><svg viewBox="0 0 12 10"><path d="M1 5.5 4.5 9 11 1.5" fill="none" stroke="var(--gold)" stroke-width="2.4"/></svg>Focused on helping plan sponsors reduce administrative burdens and fiduciary risk</li>
      <li><svg viewBox="0 0 12 10"><path d="M1 5.5 4.5 9 11 1.5" fill="none" stroke="var(--gold)" stroke-width="2.4"/></svg>Dedicated to helping employees work toward a positive retirement outcome through careful analysis of their savings rate , investment strategy and overall financial wellness</li>
    </ul>
  </section>

  <p class="abs cta">CHOOSE YOUR RETIREMENT PLAN NOW!!</p>
  <div class="abs address-bar"><span>2400 Larkspur Ave. Joliet, IL 60435</span><span>www.claireholden.com</span></div>

  <div class="abs contact">
    <svg class="contact-icon" viewBox="0 0 54 56" aria-hidden="true">
      <rect x="14" y="2" width="26" height="48" rx="4" fill="none" stroke="var(--white)" stroke-width="4"/>
      <line x1="23" y1="8" x2="31" y2="8" stroke="var(--white)" stroke-width="2.5"/>
      <circle cx="27" cy="43" r="2.5" fill="var(--white)"/>
      <path d="M4 30 Q4 22 12 22 L16 22 L16 54 L10 54 Q4 54 4 46 Z" fill="var(--white)"/>
      <rect x="36" y="26" width="12" height="6" rx="3" fill="var(--white)"/>
      <rect x="36" y="34" width="12" height="6" rx="3" fill="var(--white)"/>
      <rect x="36" y="42" width="11" height="6" rx="3" fill="var(--white)"/>
    </svg>
    <div>
      <div class="contact-phone">(815)555.0142</div>
      <div class="contact-email">c.holden@kfin.com</div>
    </div>
  </div>
</main>
</body>
</html>
```